'Tarovin' a financial/crypto-currency exchange in the middle east

On the card we need 1) Name 2) title 3) email address 4) phone number using the same colors and theme as the logo. On one side we just want the logo and we want the whole card to be in blue (same blue as logo) with the logo in the back being white.
Industry/Entity Type
Financial

```html
<!DOCTYPE html>
<html lang="en">
<head>
<meta charset="utf-8">
<title>Tarovin Business Card</title>
<link rel="stylesheet" href="https://fonts.googleapis.com/css2?family=Montserrat:wght@600;700&family=Source+Sans+3:wght@400&display=swap">
<style>
  :root {
    --backdrop: #2b2b2d;
    --brand-blue: #1a86c7;
    --front-blue: #1c84c3;
    --paper: #f7f7f7;
    --band-gray: #8a8c91;
    --ink: #4a4a4a;
    --rule: #b9b9b9;
    --white: #ffffff;
  }
  * { margin: 0; padding: 0; box-sizing: border-box; }
  html, body { width: 1200px; height: 896px; overflow: hidden; background: var(--backdrop); }
  .stage { position: relative; width: 1200px; height: 896px; }

  .card {
    position: absolute;
    width: 486px;
    height: 277px;
    border-radius: 14px;
    overflow: hidden;
  }
  .card-front { left: 354px; top: 162px; background: var(--front-blue); }
  .card-back { left: 352px; top: 469px; background: var(--paper); }

  .brand {
    position: absolute;
    display: flex;
    align-items: center;
    gap: 12px;
    font-family: "Montserrat", sans-serif;
    font-weight: 700;
    font-size: 38px;
    letter-spacing: 0.2px;
  }
  .brand-mark { width: 66px; height: 66px; border-radius: 50%; flex: none; }
  .card-front .brand { left: 128px; top: 105px; color: var(--white); }
  .card-front .brand-mark { border: 4px solid var(--white); }
  .card-back .brand { left: 25px; top: 106px; color: var(--brand-blue); }
  .card-back .brand-mark { border: 4px solid var(--brand-blue); }

  .divider {
    position: absolute;
    left: 278px; top: 77px;
    width: 1px; height: 136px;
    background: var(--rule);
  }
  .contact { position: absolute; left: 300px; top: 72px; }
  .contact-name {
    font-family: "Montserrat", sans-serif;
    font-weight: 700;
    font-size: 19px;
    color: var(--brand-blue);
    letter-spacing: 0.3px;
  }
  .contact-title, .contact-address, .contact-line {
    font-family: "Source Sans 3", sans-serif;
    font-size: 11.5px;
    color: var(--ink);
  }
  .contact-title { margin-top: 2px; }
  .contact-address { margin-top: 10px; line-height: 18px; }
  .contact-list { list-style: none; margin-top: 3px; }
  .contact-line { display: flex; align-items: center; gap: 7px; height: 18px; }
  .contact-line svg { width: 9px; height: 9px; flex: none; fill: var(--brand-blue); }

  .card-band {
    position: absolute;
    left: 0; bottom: 0;
    width: 486px; height: 42px;
    background: linear-gradient(180deg, var(--band-gray) 0%, var(--brand-blue) 45%, var(--brand-blue) 100%);
  }
</style>
</head>
<body>
<main class="stage">
  <section class="card card-front" aria-label="Card front">
    <div class="brand"><span class="brand-mark"></span><span class="brand-name">Tarovin</span></div>
  </section>

  <section class="card card-back" aria-label="Card back">
    <div class="card-band" role="img" aria-label="Decorative gray and blue wave band along the bottom edge"></div>
    <div class="brand"><span class="brand-mark"></span><span class="brand-name">Tarovin</span></div>
    <div class="divider"></div>
    <div class="contact">
      <p class="contact-name">DANIEL REYES</p>
      <p class="contact-title">President</p>
      <p class="contact-address">24 Harbor Point Drive,<br>Suite 210 &nbsp;- &nbsp;Dubai, UAE</p>
      <ul class="contact-list">
        <li class="contact-line">
          <svg viewBox="0 0 10 10"><path d="M2 0.5 L3.6 2.6 L2.8 3.6 C3.4 5 5 6.6 6.4 7.2 L7.4 6.4 L9.5 8 L8.4 9.5 C4.5 9.2 0.8 5.5 0.5 1.6 Z"/></svg>
          <span>(971) 555-0142</span>
        </li>
        <li class="contact-line">
          <svg viewBox="0 0 10 10"><path d="M0 1.5 H10 V8.5 H0 Z M0.8 2.2 L5 5.4 L9.2 2.2 Z" fill-rule="evenodd"/></svg>
          <span>daniel@tarovin.com</span>
        </li>
        <li class="contact-line">
          <svg viewBox="0 0 10 10"><circle cx="5" cy="5" r="4.5"/></svg>
          <span>www.tarovin.com</span>
        </li>
      </ul>
    </div>
  </section>
</main>
</body>
</html>
```